Medical Website - (plastic Surgery)

HERE is a "GUIDELINE" of What I need. Please, feel free to ask anything
https://www.filecrate.example/s/k8pq2mzt7w/WEBPAGE%20MANUAL.pdf

I need you to design the page, you can do it in english, I'll translate it later. I need at least these pages

homepage
profile
contact me
Main procedures pages (like Breasts) - that has links to specific procedures like breast augmentation
blog

1) Business Name and business logo:
Reginaldo Tav6res - Cirurgia Plástica
Logo:
https://www.filecrate.example/s/r3vn8qlx2d/Logo%20Gold%204M-V0-FINAL.ai

Fonts
https://www.filecrate.example/sh/w5hz1cbe9u/QWEr8TyuIoPa3-SdFgHjKlZx

Personal Pictures (notice that this are my personal pictures, it cannot be copied to use in any other place than my website)
https://www.filecrate.example/sh/p2dq6nfv4k/BXCvb-NmLkJh4Gf2-DsAqWe

I Have a image stock files, so you can just use some samples and I'll replace them later.

Actual homepage
http://192.0.2.57/reginaldo-tavares/index5.html

PSD files for some other pages
https://www.filecrate.example/sh/c9tj3xra8m/ZZP-hU712LkQw88dFrTy4Nb

2) Navigation Link Name:
www.reginaldotavares.example.br

3) Short Description
I’m a plastic surgeon. I work mostly doing aesthetic surgeries. The website will be use for me as my personal profissional website but keeping in mind that the final objective is to turn my name a “brand" linked to high quality services on plastic surgery.

4) Target Market /Audience:
85% are women, from 20 to 60 y.o.. Mostly of them with good economical condi6on, social class B, AB, A. (Almost all of them are social media connected, use smartphones, and most of them seek and think that plas6c surgery is something glamorous).

5) Webites I like

http://drvolund.example

clean design, large icons illustrating procedures

http://drvolund.example/Procedures
how this page organize procedures

http://www.harbourlinefacialclinic.example.au
How procedures are organized by pics

http://www.riverbendaestheticinstitute.example
Procedures pages
Contact page

Target Market(s)

85% are women, from 20 to 60 y.o.. Mostly of them with good economical condi6on, social class B, AB, A. (Almost all of them are social media connected, use smartphones, and most of them seek and think that plastic surgery is something glamorous).

Industry/Entity Type

Plastic

Font styles to use
Other font styles liked:
• Link already provided to the fonts

Requirements
Must have
• Use pics to illustrate procedures and fonts with enough size to older people read. As well, some people over 40 are not used to internet, so it must be user friendly, intuitive...

```html
<!DOCTYPE html>
<html lang="pt">
<head>
<meta charset="utf-8">
<title>Reginaldo Tavares – Cirurgia Plástica</title>
<link href="https://fonts.googleapis.com/css2?family=Open+Sans:wght@300;400;600;700&display=swap" rel="stylesheet">
<style>
:root{
  --gold:#c8b07a;
  --gold-dark:#b59a5e;
  --ink:#333;
  --muted:#777;
  --line:#e4e4e4;
  --footer:#2b231c;
  --footer-deep:#1f1914;
  --footer-panel:#241d17;
  --white:#fff;
}
*{box-sizing:border-box;margin:0;padding:0}
html,body{width:1200px;height:2951px;overflow:hidden}
body{font-family:"Open Sans",Arial,sans-serif;color:var(--ink);background:var(--white);position:relative}
.abs{position:absolute}
a{color:inherit;text-decoration:none}

/* top bar + nav */
.topbar{height:28px;display:flex;align-items:center;justify-content:space-between;padding:0 40px;font-size:11px;color:#888}
.topbar .contacts span{margin-right:18px}
.topbar .account span{margin-left:18px}
.header{height:72px;display:flex;align-items:center;justify-content:space-between;padding:0 12px 0 56px;border-bottom:1px solid var(--line)}
.brand{display:flex;align-items:center;gap:12px}
.brand-mark{width:40px;height:40px;border-radius:50%;background:var(--gold)}
.brand-name{font-size:26px;font-weight:600;color:#222;letter-spacing:-.3px}
.nav{display:flex;gap:26px;font-size:14px;color:#333}
.nav .active{color:var(--gold);position:relative}
.nav .active::before{content:"";position:absolute;left:50%;top:-28px;width:56px;margin-left:-28px;height:2px;background:var(--gold)}

/* hero */
.hero{top:100px;left:0;width:1200px;height:408px;background:linear-gradient(90deg,#a9a9a9,#cfcfcf 45%,#d9d9d9 70%,#bdbdbd)}
.hero-copy{left:150px;top:170px;width:330px;text-align:center;color:var(--white)}
.hero-copy h1{font-weight:300;font-size:40px;line-height:60px}
.hero-copy .tagline{margin-top:14px;padding:8px 0;border-top:1px solid rgba(255,255,255,.8);border-bottom:1px solid rgba(255,255,255,.8);font-size:15px}
.hero-btns{left:192px;top:378px;display:flex;gap:12px}
.btn{display:inline-block;background:var(--gold);color:var(--white);font-size:14px;text-align:center}
.hero-btns .btn{width:128px;height:36px;line-height:36px}
.arrow{width:30px;height:44px;background:rgba(0,0,0,.18)}

/* specialties */
.section-title{font-weight:300;text-align:center;font-size:40px;color:#222}
.spec-title{top:520px;left:0;width:1200px}
.spec-intro{top:580px;left:140px;width:920px;text-align:center;font-size:15px;line-height:28px;color:var(--muted)}
.spec-grid{top:669px;left:47px;display:flex;gap:26px}
.spec-card{width:200px;height:202px;position:relative;background:linear-gradient(135deg,#e7cfbe,#caa68e)}
.spec-card span{position:absolute;left:0;bottom:12px;width:112px;height:28px;line-height:28px;padding-left:30px;background:rgba(200,176,122,.88);color:var(--white);font-size:15px;font-weight:600}

/* cta band */
.cta{top:915px;left:0;width:1200px;height:128px;background:var(--gold);color:var(--white)}
.cta h2{position:absolute;left:84px;top:20px;font-size:22px;font-weight:400}
.cta p{position:absolute;left:48px;top:62px;width:690px;font-size:15px;line-height:22px}
.cta .btn-outline{position:absolute;left:878px;top:48px;width:198px;height:42px;line-height:42px;background:var(--white);color:var(--gold);text-align:center;font-size:14px;font-weight:700;letter-spacing:1px}

/* doctor */
.doctor-photo{top:1092px;left:118px;width:236px;height:324px;background:linear-gradient(180deg,#f2f2f2,#dcdcdc)}
.doctor-name{top:1145px;left:468px;font-size:17px;font-weight:700}
.doctor-bio{top:1200px;left:468px;width:570px;font-size:15.5px;line-height:17px;color:#444}
.doctor-bio p+p{margin-top:17px}
.doctor-more{top:1430px;left:826px;width:198px;height:40px;line-height:40px;font-weight:700;letter-spacing:1px}

/* booking */
.booking-bg{top:1500px;left:0;width:1200px;height:330px;background:linear-gradient(90deg,#8e847c,#b4aaa2 40%,#cfc5bd 70%,#9f9690)}
.booking{top:1518px;left:301px;width:580px;height:312px;background:rgba(35,30,26,.82)}
.booking h3{position:absolute;left:80px;top:40px;color:var(--gold);font-size:15px;font-weight:700;letter-spacing:.5px}
.field{position:absolute;height:32px;background:#f2f2f2;border:1px solid #ddd;font-size:12px;color:#aaa;padding:7px 12px}
.select{background:#e8e8e8}
.select::after{content:"▾";position:absolute;right:10px;top:7px;color:#999}
.booking .submit{position:absolute;left:344px;top:176px;width:162px;height:40px;line-height:40px}
.booking .submit b{font-size:15px}
.booking .submit small{font-size:10px;margin-left:4px}

/* news */
.news-title{top:1870px;left:0;width:1200px}
.title-rule{top:1928px;left:545px;width:110px;height:3px;background:var(--gold)}
.news-arrow{color:var(--gold);font-size:44px;font-weight:300}
.news-card{top:1979px;width:264px}
.news-card .thumb{height:152px;background:linear-gradient(135deg,#f0ebe6,#d8cfc6)}
.news-card h4{margin-top:40px;color:var(--gold);font-size:17px;font-weight:700}
.news-card p{margin-top:30px;font-size:11.5px;line-height:20px;color:#666}
.news-card .btn{margin-top:14px;width:128px;height:30px;line-height:30px;font-size:12px}

/* newsletter */
.newsletter{top:2392px;left:0;width:1200px;height:100px;background:var(--gold)}
.newsletter .label{position:absolute;left:167px;top:40px;color:var(--white);font-size:14.5px;font-weight:700}
.newsletter .input{position:absolute;left:651px;top:30px;width:253px;height:40px;background:var(--white);color:#aaa;font-size:13px;padding:11px 20px}
.newsletter .go{position:absolute;left:904px;top:30px;width:116px;height:40px;line-height:40px;background:#a88c52;color:var(--white);text-align:center;font-size:14px}

/* footer */
.footer{top:2492px;left:0;width:1200px;height:390px;background:var(--footer)}
.footer h5{position:absolute;top:48px;font-size:20px;font-weight:400;color:var(--white)}
.footer h5 b{font-weight:700}
.links{position:absolute;top:98px;width:220px;list-style:none}
.links li{height:39.5px;line-height:40px;font-size:12.5px;color:#c9c2b8;border-bottom:1px solid #443a31}
.links li.hl{color:var(--gold)}
.widget{position:absolute;left:633px;top:97px;width:252px;height:240px;background:var(--white);padding:8px 10px;font-size:11px;color:#333}
.widget .head{font-weight:700;border-bottom:1px solid #ddd;padding-bottom:6px}
.widget .page{display:flex;gap:8px;margin-top:8px;align-items:flex-start}
.widget .page i{width:36px;height:36px;background:#d8d8d8;display:block}
.widget .page b{color:#3b5998}
.widget .faces{display:grid;grid-template-columns:repeat(5,1fr);gap:8px 6px;margin-top:10px}
.widget .faces div{height:34px;background:#cfcfcf}
.widget .faces span{font-size:8px;text-align:center;color:#555;margin-top:-6px}
.panel{position:absolute;left:907px;top:0;width:240px;height:390px;background:var(--footer-panel);color:var(--white)}
.panel .brand-name{color:var(--white);font-size:21px;text-align:center;margin-top:66px}
.panel .motto{margin:60px 0 0 26px;font-size:25px;line-height:27px;font-weight:400}
.socials{display:flex;gap:6px;margin:40px 0 0 26px}
.socials i{width:20px;height:20px;border-radius:50%;background:#8a8278;display:block}
.bottombar{top:2882px;left:0;width:1200px;height:69px;background:var(--footer-deep);color:#c9c2b8;font-size:12px}
.bottombar .copy{position:absolute;left:112px;top:26px}
.bottombar .copy b{color:var(--white)}
.bottombar .menu{position:absolute;left:698px;top:28px}
</style>
</head>
<body>

<div class="topbar">
  <div class="contacts"><span>☎ Contacte-nos: (047) 5550-0142</span><span>✉ Email : info@reginaldotavares.example.br</span></div>
  <div class="account"><span>Acessar</span><span>Registrar</span></div>
</div>
<header class="header">
  <div class="brand"><i class="brand-mark"></i><span class="brand-name">Reginaldo Tavares</span></div>
  <nav class="nav">
    <a class="active">Home</a><a>Equipe ⌄</a><a>Face</a><a>⌄ Mama</a><a>Corpo</a><a>⌄ Homens ⌄</a><a>Estética ⌄</a><a>Contactos &amp; Marcações ⌄</a>
  </nav>
</header>

<section class="hero abs" role="img" aria-label="Hero photo: woman's face with mirrored tile panels on a grey wall"></section>
<div class="hero-copy abs">
  <h1>Descubra<br>o seu novo “eu”</h1>
  <div class="tagline">Beleza, Simetria, Equilíbrio, Proporção</div>
</div>
<div class="hero-btns abs"><a class="btn">Contacte-nos</a><a class="btn">Saiba mais</a></div>
<svg class="abs" style="left:10px;top:278px" width="30" height="44"><rect width="30" height="44" fill="rgba(0,0,0,.15)"/><path d="M19 14 11 22l8 8" stroke="#fff" stroke-width="2" fill="none"/></svg>
<svg class="abs" style="left:1160px;top:278px" width="30" height="44"><rect width="30" height="44" fill="rgba(0,0,0,.15)"/><path d="M11 14l8 8-8 8" stroke="#fff" stroke-width="2" fill="none"/></svg>

<h2 class="section-title spec-title abs">Especialidades</h2>
<p class="spec-intro abs">Lorem ipsum dolor sit amet, consectetur adipiscing elit. Nam scelerisque faucibus risus non iaculis. Fusce a augue ante, pellentesque pretium erat. Fusce in turpis in velit tempor pretium. Integer a leo libero.</p>
<div class="spec-grid abs">
  <div class="spec-card" role="img" aria-label="Photo for face procedures"><span>Face</span></div>
  <div class="spec-card" role="img" aria-label="Photo for breast procedures"><span>Mama</span></div>
  <div class="spec-card" role="img" aria-label="Photo for body procedures"><span>Corpo</span></div>
  <div class="spec-card" role="img" aria-label="Photo for men's procedures"><span>Homens</span></div>
  <div class="spec-card" role="img" aria-label="Photo for aesthetic treatments"><span>Estética</span></div>
</div>

<section class="cta abs">
  <h2>Venha saber o que podemos fazer por si, sem custo.</h2>
  <p>Lorem ipsum dolor sit amet, consectetur adipiscing elit. Praesent convallis, nunc et tristique lobortis, libero nisl ullamcorper libero, non tincidunt neque leo sit amet lacus.</p>
  <a class="btn-outline">MARCAÇÕES</a>
</section>

<div class="doctor-photo abs" role="img" aria-label="Portrait of the surgeon in a white coat with stethoscope"></div>
<h3 class="doctor-name abs">Dr. Reginaldo Tavares</h3>
<div class="doctor-bio abs">
  <p>Lorem ipsum dolor sit amet, consectetur adipiscing elit. Integer vehicula lacinia ipsum et accumsan. Aenean orci lorem, malesuada at dolor sed, feugiat mattis purus. Nam ac dui eu dui scelerisque bibendum in nec ipsum. Fusce viverra arcu ut dui vehicula, non facilisis ante rhoncus. Praesent sit amet felis gravida velit venenatis luctus eget et purus. Morbi enim neque, tincidunt iaculis neque sit amet, bibendum vestibulum ligula. Sed convallis ligula vel turpis sodales, sit amet iaculis dui pretium. Fusce tempus neque nec euismod viverra.</p>
  <p>Morbi enim neque, tincidunt iaculis neque sit amet, bibendum vestibulum ligula. Sed convallis ligula vel turpis sodales, sit amet iaculis dui pretium. Fusce tempus neque nec euismod viverra.</p>
</div>
<a class="btn doctor-more abs">LER MAIS</a>

<div class="booking-bg abs" role="img" aria-label="Photo of clinic staff and a receptionist wearing a headset"></div>
<form class="booking abs">
  <h3>AGENDAMENTO DE CONSULTAS</h3>
  <div class="field" style="left:68px;top:84px;width:240px">Nome Completo</div>
  <div class="field" style="left:68px;top:121px;width:240px">Email</div>
  <div class="field" style="left:68px;top:158px;width:240px">Telefone</div>
  <div class="field select" style="left:344px;top:84px;width:182px">Consultório</div>
  <div class="field select" style="left:344px;top:121px;width:182px">Procedimento</div>
  <a class="btn submit"><b>Marcar</b><small>ver horários</small></a>
</form>

<h2 class="section-title news-title abs">Notícias e Artigos</h2>
<div class="title-rule abs"></div>
<div class="news-arrow abs" style="left:70px;top:2020px">&lt;</div>
<div class="news-arrow abs" style="left:1092px;top:2020px">&gt;</div>
<article class="news-card abs" style="left:138px">
  <div class="thumb" role="img" aria-label="Photo of a woman's waist holding fruit"></div>
  <h4>LOREM IPSUM</h4>
  <p>Sed a velit vitae nunc porta iaculis. Aliquam tempus rutrum diam, non tincidunt odio pharetra vitae. Nulla facilisi. Duis sed laoreet dui. Duis a risus nec erat tincidunt feugiat. Cras dui velit, luctus vitae volutpat vitae.</p>
  <a class="btn">Read more</a>
</article>
<article class="news-card abs" style="left:466px">
  <div class="thumb" role="img" aria-label="Photo of a woman receiving a cosmetic injection"></div>
  <h4>LOREM IPSUM</h4>
  <p>Sed a velit vitae nunc porta iaculis. Aliquam tempus rutrum diam, non tincidunt odio pharetra vitae. Nulla facilisi. Duis sed laoreet dui. Duis a risus nec erat tincidunt feugiat. Cras dui velit, luctus vitae volutpat vitae.</p>
  <a class="btn">Read more</a>
</article>
<article class="news-card abs" style="left:791px">
  <div class="thumb" role="img" aria-label="Photo of the surgeon standing with arms crossed"></div>
  <h4>LOREM IPSUM</h4>
  <p>Sed a velit vitae nunc porta iaculis. Aliquam tempus rutrum diam, non tincidunt odio pharetra vitae. Nulla facilisi. Duis sed laoreet dui. Duis a risus nec erat tincidunt feugiat. Cras dui velit, luctus vitae volutpat vitae.</p>
  <a class="btn">Read more</a>
</article>

<section class="newsletter abs">
  <span class="label">Subcreva a Newsletter para receber notícias e dicas sobre saúde.</span>
  <div class="input">Add your email adress</div>
  <a class="go">Subcrever</a>
</section>

<footer class="footer abs">
  <h5 style="left:112px">Lista de <b>Intervenções</b></h5>
  <ul class="links" style="left:112px">
    <li>FACE</li><li>CORPO</li><li>MAMAS</li><li>ESTÉTICA</li><li>PELE</li><li>AGENDAMENTO DE CONSULTAS</li>
  </ul>
  <h5 style="left:376px">Saiba <b>Mais</b></h5>
  <ul class="links" style="left:376px">
    <li>NOTICIAS &amp; BLOG</li><li>PROCEDIMENTOS CIRURGICOS</li><li>CLINICAS</li><li>EQUIPA</li><li class="hl">PERGUNTAS FREQUENTES</li><li>CONTACTOS</li>
  </ul>
  <div class="widget">
    <div class="head">Find us on Socialnet</div>
    <div class="page"><i></i><div><b>Socialnet Page</b><br><span style="font-size:10px">Like</span></div></div>
    <div style="margin-top:8px;font-size:10px">1,988,819 people like Socialnet Page.</div>
    <div class="faces">
      <div></div><div></div><div></div><div></div><div></div>
      <span>Sergi</span><span>Giorgia</span><span>Henry</span><span>Osman</span><span>Ruth</span>
      <div></div><div></div><div></div><div></div><div></div>
      <span>Daniel</span><span>Elina</span><span>Pius</span><span>Ashley</span><span>Marco</span>
    </div>
  </div>
  <div class="panel">
    <div class="brand-name">Reginaldo Tavares</div>
    <p class="motto">A DELICADA<br>ARTE DE<br>EQUILIBRAR A<br>CIÊNCIA COM A<br>NATUREZA</p>
    <div class="socials"><i></i><i></i><i></i><i></i><i></i><i></i><i></i></div>
  </div>
</footer>
<div class="bottombar abs">
  <span class="copy"><b>Copyright 2014</b> - Reginaldo Tavares. Todos os direitos reservados.</span>
  <span class="menu">Blog | Media | Perguntas Frequentes | Contactos</span>
</div>

</body>
</html>
```